Inspirational Quotes Poster Set

Norbelle is a stylish coworking space, which has a design-oriented vintage look from the 60's with an industrial touch (www.norbelle-example.com) Norbelle Quote Poster Set of 16 posters. The poster should be typo oriented and rather simple. Reflecting a bit the clean billboard design from the sixties. Minimal / simple graphical elements

Target Market(s)

Startups and Entrepreneurs

Industry/Entity Type

Startup

Font styles to use
Sans Serif

Colors

Designer to choose colors to be used in the design.

Requirements
Must have
• Posters need to be on and very stylish

```html
<!DOCTYPE html>
<html lang="en">
<head>
<meta charset="utf-8">
<title>Norbelle Quote Poster Set – Learn by Doing</title>
<link rel="stylesheet" href="https://fonts.googleapis.com/css2?family=Bebas+Neue&family=Carlito:wght@400&display=swap">
<style>
  :root {
    --poster-yellow: #f4ea5a;
    --ink: #000000;
    --figure-tone: #e4d84a;
  }
  html, body {
    margin: 0;
    padding: 0;
    overflow: hidden;
    background: var(--poster-yellow);
  }
  .poster {
    position: relative;
    width: 738px;
    height: 1200px;
    background: var(--poster-yellow);
    color: var(--ink);
    overflow: hidden;
  }
  .quote-line {
    position: absolute;
    left: 0;
    width: 716px;
    margin: 0;
    text-align: center;
    font-family: "Bebas Neue", "Oswald", sans-serif;
    font-weight: 400;
    line-height: 1;
    white-space: nowrap;
  }
  .line-you       { top: 49px;  font-size: 107px; }
  .line-dont      { top: 148px; font-size: 86px; }
  .line-walk      { top: 236px; font-size: 148px; }
  .line-rules     { top: 384px; font-size: 86px; }
  .line-learn-by  { top: 470px; font-size: 115px; }
  .line-doing     { top: 584px; font-size: 151px; }
  .line-falling   { top: 721px; font-size: 117px; }

  .crawling-figure {
    position: absolute;
    left: 254px;
    top: 876px;
    width: 240px;
    height: 152px;
    border-radius: 60px;
    background: var(--figure-tone);
  }

  .attribution {
    position: absolute;
    left: 0;
    top: 1050px;
    width: 712px;
    margin: 0;
    text-align: center;
    font-family: "Carlito", "Open Sans", sans-serif;
    font-size: 46px;
    line-height: 54px;
    color: var(--ink);
  }
  .attribution span { display: block; }
</style>
</head>
<body>
  <main class="poster">
    <h1 class="quote-line line-you">You</h1>
    <p class="quote-line line-dont">Don’t learn to</p>
    <p class="quote-line line-walk">Walk</p>
    <p class="quote-line line-rules">By following rules</p>
    <p class="quote-line line-learn-by">You learn by</p>
    <p class="quote-line line-doing">Doing</p>
    <p class="quote-line line-falling">And falling over</p>

    <div class="crawling-figure" role="img" aria-label="Simple line icon of a crawling baby"></div>

    <p class="attribution">
      <span class="author-name">Rowan Ashby</span>
      <span class="author-role">Halcyon Group Founder</span>
    </p>
  </main>
</body>
</html>
```